TRV Conference Newsletter Postcard

We need a template design for a direct mailer postcard that we are sending to potential attendees. The attached templates include the dimensions of the postcard. It is a panel/map type of postcard so it has 8 surfaces that need to have content on them. The purpose of this project is to get people to sign up and attend our conference in May. I have attached what type of layout we would like to have on each panel of the postcard.

Target Market(s)

Category Managers, Shopper Insights, Shopper Marketing

Industry/Entity Type

Consumer

Font styles to use
Sans Serif

Requirements
Must have
• A fun but clean template that includes designs, graphics, elements that show lists, our agenda, pop up graphics that can show facts and stats.
• An interesting shopper cart graphic that include insights, analytics, data, networking, etc.
Nice to have
• Maybe some fun content based on the conference title.
Should not have
• No animated characters. We want this to be clean and innovative, but fun.

```html
<!DOCTYPE html>
<html lang="en">
<head>
<meta charset="utf-8">
<title>TRV Conference Postcard</title>
<link rel="stylesheet" href="https://fonts.googleapis.com/css2?family=Roboto:wght@300;400;500;700;900&family=Roboto+Condensed:wght@400;700&display=swap">
<style>
:root{
  --stage:#c9cacf;
  --paper:#ffffff;
  --navy:#0b1c44;
  --navy-2:#10306b;
  --blue:#1e86d3;
  --blue-bright:#2ea3e6;
  --blue-title:#1a5e9e;
  --sky:#5bb4ec;
  --amber:#f7b500;
  --ink:#222831;
  --grey:#d9dadd;
  --red:#d32027;
}
*{box-sizing:border-box;margin:0;padding:0}
html,body{width:1200px;height:1200px;overflow:hidden;background:var(--stage);font-family:"Roboto",sans-serif;color:var(--ink)}
.canvas{position:relative;width:1200px;height:1200px}
.sheet{position:absolute;left:172px;width:855px;height:554px;background:var(--paper)}
.sheet--outer{top:35px}
.sheet--inner{top:618px}
.abs{position:absolute}

/* ---------- outer sheet ---------- */
.welcome{left:11px;top:11px;width:416px;height:265px;background:linear-gradient(180deg,#c4c6ca,#e3e4e6);text-align:center}
.hero-graphic{position:absolute;left:67px;top:10px;width:270px;height:96px;background:radial-gradient(ellipse at center,#1ea6f0 0%,#1a7fd0 45%,rgba(60,160,230,.35) 75%,rgba(255,255,255,0) 100%)}
.event-title{font-weight:700;font-size:15px;color:var(--blue-title);letter-spacing:.2px}
.event-sub{font-weight:300;font-size:10px;color:var(--blue-bright);letter-spacing:2px;margin-top:3px}
.welcome .event-title{position:absolute;left:0;right:0;top:122px}
.welcome .event-sub{position:absolute;left:0;right:0;top:140px;margin:0}
.welcome-copy{position:absolute;left:0;right:0;top:170px;font-weight:500;font-size:12.5px;line-height:17px;color:#1d1f24}

.member-banner{left:39px;top:298px;width:349px;height:69px;background:linear-gradient(90deg,#8a9bc8,#6a7fb5 40%,#c9cfe0 75%,#a89c94)}
.member-banner span{position:absolute;left:128px;top:18px;font-weight:300;font-size:14px;line-height:17px;color:#fff}
.address-lines{left:87px;width:251px}
.address-lines i{display:block;height:1px;background:#bdbdbd;margin-bottom:38px}

.about-photo{left:427px;top:11px;width:243px;height:170px;background:linear-gradient(180deg,#3b3b3e,#101012)}
.about-title{left:442px;top:100px;font-family:"Roboto Condensed",sans-serif;font-weight:700;font-size:17px;line-height:17px;color:var(--amber);text-transform:uppercase}
.bullets{left:444px;top:199px;list-style:none}
.bullets li{position:relative;font-size:6px;line-height:11.2px;padding-left:14px;color:#333}
.bullets svg{position:absolute;left:0;top:1px}

.cover{left:670px;top:11px;width:174px;height:265px;background:#eeeff1}
.cover-graphic{left:9px;top:20px;width:155px;height:52px;background:radial-gradient(ellipse at center,#1ea6f0 0%,#1a7fd0 45%,rgba(60,160,230,.3) 75%,rgba(255,255,255,0) 100%)}
.cover .event-title{position:absolute;left:0;right:0;top:96px;font-size:9px;text-align:center}
.cover .event-sub{position:absolute;left:0;right:0;top:107px;font-size:6px;letter-spacing:1px;text-align:center;margin:0}
.cover-blurb{left:-16px;top:144px;width:179px;height:82px;background:var(--blue);color:#fff;font-size:6.2px;line-height:7.7px;padding:8px 6px;font-weight:500}
.venue{display:flex;align-items:center;gap:5px}
.venue-name{text-align:right;font-size:6.5px;font-weight:700;line-height:7.5px;color:#333}
.venue-name small{display:block;font-size:5px;font-weight:500}
.venue-date{border-left:1.5px solid var(--blue-title);padding-left:5px;font-family:"Roboto Condensed",sans-serif;font-weight:700;color:var(--blue-title);font-size:16px;line-height:13px}
.venue-date small{display:block;font-size:10px;line-height:10px}
.cover .venue{position:absolute;right:10px;top:233px}

.topics{left:427px;top:276px;width:417px;height:267px;background:linear-gradient(180deg,#0a1a3e,#122e66)}
.topics-band{position:absolute;left:0;top:0;width:100%;height:69px;background:linear-gradient(90deg,#0b1b40,#14306a 55%,#1d4c94)}
.band-mark{position:absolute;left:10px;top:10px;width:78px;font-family:"Roboto Condensed",sans-serif;font-weight:700;font-size:8.5px;line-height:8.5px;color:#fff;text-align:right;border-right:1px solid #3a5a90;padding-right:8px}
.band-mark span{display:block;font-family:"Roboto",sans-serif;font-weight:300;font-size:8px;color:var(--sky);letter-spacing:1px}
.band-graphic{position:absolute;left:90px;top:10px;width:110px;height:50px;background:radial-gradient(ellipse at 40% 50%,#22aef2 0%,#1a7fd0 45%,rgba(30,120,200,0) 80%)}
.band-title{position:absolute;left:211px;top:22px;font-size:11px;line-height:12px;color:var(--sky);font-weight:400;text-transform:uppercase}
.topic-grid{position:absolute;left:26px;top:90px;display:grid;grid-template-columns:198px 198px;column-gap:0;row-gap:30px}
.topic h3{font-family:"Roboto Condensed",sans-serif;font-weight:700;font-size:16px;color:var(--blue-bright);text-align:center;letter-spacing:.3px}
.topic p{font-size:5.5px;line-height:7.2px;color:#d8e4f5;text-align:center;margin-top:3px}

/* ---------- inner sheet ---------- */
.inner-band{left:11px;top:12px;width:833px;height:65px;background:var(--blue)}
.inner-band h2{position:absolute;font-family:"Roboto Condensed",sans-serif;font-weight:700;color:#fff;text-transform:uppercase}
.agenda-title{left:75px;top:20px;font-size:21px}
.lineup-title{left:442px;top:19px;font-size:16.5px;line-height:17px}
.inner-band .venue{position:absolute;right:14px;top:21px}
.inner-band .venue-name,.inner-band .venue-date{color:#fff;border-color:#fff}

.agenda{left:11px;top:77px;width:416px;height:466px;background:radial-gradient(ellipse at 50% 75%,#2a7fd4 0%,#13408e 40%,#0a1d46 80%)}
.day-col{position:absolute;top:14px}
.day-tab{display:flex;width:101px;height:22px;background:var(--navy-2);border:1.5px solid var(--blue-bright);color:#fff;font-size:7.5px;line-height:8px;padding:3px 4px;gap:6px;margin-left:2px}
.day-tab div+div{border-left:1px solid #9cc8f0;padding-left:6px}
.day-tab b{display:block;font-weight:700}
.slots{list-style:none;border-left:1.5px solid #8fb5e0;margin:8px 0 0 14px;padding-left:12px}
.slots li{position:relative;min-height:32px;font-size:7.5px;line-height:8px;color:#fff}
.slots li::before{content:"";position:absolute;left:-12px;top:4px;width:8px;height:1.5px;background:#8fb5e0}
.slots b{display:block;font-weight:700;font-size:8px}
.slots small{display:block;font-size:5.5px;line-height:6px;padding-left:3px}
.day-col .day-tab.again{margin-top:4px}
.brand-seal{position:absolute;right:8px;bottom:8px;width:38px;height:38px;border-radius:50%;background:#fff;display:flex;align-items:center;justify-content:center;font-weight:700;font-size:10px;color:var(--navy)}

.lineup{left:427px;top:77px;width:417px;height:312px;background:linear-gradient(160deg,#ffffff,#f0f1f4 60%,#e4e6ea)}
.speaker{position:absolute;width:140px;text-align:center}
.portrait{width:70px;height:70px;margin:0 auto;border-radius:50%;border:2px solid var(--blue);background:linear-gradient(180deg,#d6d9de,#9aa0a9)}
.speaker h4{font-family:"Roboto Condensed",sans-serif;font-weight:700;font-size:9.5px;color:var(--blue-title);margin-top:4px}
.speaker .role{font-family:"Roboto Condensed",sans-serif;font-size:7.5px;color:var(--blue)}
.speaker .cred{font-family:"Roboto Condensed",sans-serif;font-size:4.6px;line-height:6px;color:#444}

.promo{left:427px;top:389px;width:417px;height:118px;background:linear-gradient(180deg,#2a8fd8,#0f4f9c)}
.stat-box{position:absolute;top:11px;width:131px;height:97px;background:#fff;color:var(--blue);font-weight:300;font-size:12.5px;line-height:12.5px;text-align:center;padding-top:10px}
.discount{position:absolute;left:318px;top:-28px;width:80px;height:80px;border-radius:50%;background:#fff;border:3px solid var(--blue);text-align:center;padding-top:10px}
.discount b{display:block;font-family:"Roboto Condensed",sans-serif;font-weight:700;font-size:28px;line-height:26px;color:var(--red)}
.discount span{display:block;font-weight:700;font-size:11px;line-height:12px;color:var(--navy)}
.discount small{display:block;font-size:5.5px;line-height:6.5px;font-weight:700;color:var(--navy);letter-spacing:.5px}
.promo-note{position:absolute;left:300px;top:67px;width:112px;text-align:center;color:#fff;font-size:9.5px;line-height:10px}
.sponsors{left:427px;top:507px;width:417px;height:36px;background:#fff;display:flex;align-items:center;justify-content:center;gap:12px}
.sponsors i{display:block;width:18px;height:10px;background:#b9bcc2;border-radius:2px}
.sponsors i.round{width:11px;height:11px;border-radius:50%}
</style>
</head>
<body>
<main class="canvas">

  <!-- OUTER SHEET -->
  <section class="sheet sheet--outer">
    <div class="abs welcome">
      <div class="hero-graphic" role="img" aria-label="Shopping cart emblem surrounded by flying blue data tiles"></div>
      <div class="event-title">BRIDGING TRADITIONAL &amp; DIGITAL:</div>
      <div class="event-sub">CREATING NEW PATHS TO SUCCESS</div>
      <p class="welcome-copy">We look forward to seeing you in MAY!<br>“Questions? Contact us at<br>members@trvforum.org or call 555.014.2290<br>Visit www.trvforum.example<br>for more information about the TRV!</p>
    </div>

    <div class="abs member-banner" role="img" aria-label="Colourful gear graphic and a member holding a membership card">
      <span>Welcome to<br>&nbsp;&nbsp;&nbsp;&nbsp;&nbsp;the TRV!</span>
    </div>

    <div class="abs address-lines" style="top:469px">
      <i></i><i></i><i></i>
    </div>

    <div class="abs about-photo" role="img" aria-label="Audience photo at a conference keynote"></div>
    <h2 class="abs about-title">About the 2017<br>Category Management &amp;<br>Shopper Insights<br>Conference</h2>

    <ul class="abs bullets">
      <li><svg width="10" height="8" viewBox="0 0 10 8"><path d="M0 1h2l1.5 4h5L10 2H3" fill="none" stroke="#1e86d3" stroke-width="1"/><circle cx="4" cy="7" r=".8" fill="#1e86d3"/><circle cx="8" cy="7" r=".8" fill="#1e86d3"/></svg>These are the bullet points. These are the bullet points.</li>
      <li><svg width="10" height="8" viewBox="0 0 10 8"><path d="M0 1h2l1.5 4h5L10 2H3" fill="none" stroke="#1e86d3" stroke-width="1"/><circle cx="4" cy="7" r=".8" fill="#1e86d3"/><circle cx="8" cy="7" r=".8" fill="#1e86d3"/></svg>These are the bullet points. These are the bullet points.</li>
      <li><svg width="10" height="8" viewBox="0 0 10 8"><path d="M0 1h2l1.5 4h5L10 2H3" fill="none" stroke="#1e86d3" stroke-width="1"/><circle cx="4" cy="7" r=".8" fill="#1e86d3"/><circle cx="8" cy="7" r=".8" fill="#1e86d3"/></svg>These are the bullet points. These are the bullet points.</li>
      <li><svg width="10" height="8" viewBox="0 0 10 8"><path d="M0 1h2l1.5 4h5L10 2H3" fill="none" stroke="#1e86d3" stroke-width="1"/><circle cx="4" cy="7" r=".8" fill="#1e86d3"/><circle cx="8" cy="7" r=".8" fill="#1e86d3"/></svg>These are the bullet points. These are the bullet points.</li>
      <li><svg width="10" height="8" viewBox="0 0 10 8"><path d="M0 1h2l1.5 4h5L10 2H3" fill="none" stroke="#1e86d3" stroke-width="1"/><circle cx="4" cy="7" r=".8" fill="#1e86d3"/><circle cx="8" cy="7" r=".8" fill="#1e86d3"/></svg>These are the bullet points. These are the bullet points.</li>
      <li><svg width="10" height="8" viewBox="0 0 10 8"><path d="M0 1h2l1.5 4h5L10 2H3" fill="none" stroke="#1e86d3" stroke-width="1"/><circle cx="4" cy="7" r=".8" fill="#1e86d3"/><circle cx="8" cy="7" r=".8" fill="#1e86d3"/></svg>These are the bullet points. These are the bullet points.</li>
    </ul>

    <div class="abs cover">
      <div class="abs cover-graphic" role="img" aria-label="Shopping cart emblem with blue data tiles"></div>
      <div class="event-title">BRIDGING TRADITIONAL &amp; DIGITAL:</div>
      <div class="event-sub">CREATING NEW PATHS TO SUCCESS</div>
      <p class="abs cover-blurb">Then leave space for a paragraph of about 8 lines. Then leave space for a paragraph of about 8 lines. Then leave space for a paragraph of about 8 lines. Then leave space for a paragraph of about 8 lines. Then leave space for a paragraph of about 8 lines. Then leave space for a paragraph of about 8 lines.</p>
      <div class="venue">
        <div class="venue-name">HARBOR GRAND<small>LAKEVIEW<br>NV</small></div>
        <div class="venue-date">MAY<small>2017</small></div>
      </div>
    </div>

    <div class="abs topics">
      <div class="topics-band">
        <div class="band-mark">BRIDGING TRADITIONAL &amp; DIGITAL:<span>CREATING NEW PATHS TO SUCCESS</span></div>
        <div class="band-graphic" role="img" aria-label="Shopping cart emblem with blue data tiles"></div>
        <div class="band-title">Category Management &amp;<br>Shopper Insights Conference</div>
      </div>
      <div class="topic-grid">
        <div class="topic"><h3>THIS IS HEADER 01</h3><p>Short topic summary goes here in two lines<br>of supporting copy for this session block</p></div>
        <div class="topic"><h3>THIS IS HEADER 04</h3><p>Short topic summary goes here in two lines<br>of supporting copy for this session block</p></div>
        <div class="topic"><h3>THIS IS HEADER 02</h3><p>Short topic summary goes here in two lines<br>of supporting copy for this session block</p></div>
        <div class="topic"><h3>THIS IS HEADER 05</h3><p>Short topic summary goes here in two lines<br>of supporting copy for this session block</p></div>
        <div class="topic"><h3>THIS IS HEADER 03</h3><p>Short topic summary goes here in two lines<br>of supporting copy for this session block</p></div>
        <div class="topic"><h3>THIS IS HEADER 06</h3><p>Short topic summary goes here in two lines<br>of supporting copy for this session block</p></div>
      </div>
    </div>
  </section>

  <!-- INNER SHEET -->
  <section class="sheet sheet--inner">
    <div class="abs inner-band">
      <h2 class="agenda-title">2017 Agenda at a Glance</h2>
      <h2 class="lineup-title">Meet this year’s starting<br>speaker line up!</h2>
      <div class="venue">
        <div class="venue-name">HARBOR GRAND<small>LAKEVIEW<br>NV</small></div>
        <div class="venue-date">MAY<small>2017</small></div>
      </div>
    </div>

    <div class="abs agenda">
      <div class="day-col" style="left:11px">
        <div class="day-tab"><div>Monday<b>5/15</b></div><div>Main<b>Conference</b></div></div>
        <ul class="slots">
          <li><b>1:00 - 2:15 PM</b>Speed Networking</li>
          <li><b>2:30 - 3:00 PM</b>Opening Welcome</li>
          <li><b>3:00 - 3:30 PM</b>Keynote Speaker</li>
          <li><b>3:30 - 4:00 PM</b>Keynote Speaker</li>
          <li><b>4:00 - 4:20 PM</b>Break</li>
          <li><b>4:20 - 5:05 PM</b>Breakout Sessions</li>
          <li style="min-height:48px"><b>5:15 - 6:15 PM</b>Solution Provider Demos<small>*3 rounds,15 min rotations,<br>5 min in between</small></li>
          <li style="min-height:30px"><b>6:15 - 7:30 PM</b>Networking Reception<br>&amp; Hors d’ouvres</li>
        </ul>
        <div class="day-tab again"><div>Tuesday<b>5/16</b></div><div>Main<b>Conference</b></div></div>
        <ul class="slots">
          <li style="min-height:34px"><b>7:00 - 8:30 AM</b>Networking Breakfast</li>
          <li><b>8:30 - 8:45 AM</b>The Days Highlights</li>
          <li><b>8:45 - 9:30 AM</b>Keynote Speaker</li>
        </ul>
      </div>

      <div class="day-col" style="left:152px">
        <div class="day-tab"><div>Tuesday<b>5/16</b></div><div>Main<b>Conference</b></div></div>
        <ul class="slots">
          <li><b>9:30 - 10:00 AM</b>Keynote Speaker</li>
          <li><b>10:00 - 10:20 AM</b>Break</li>
          <li><b>10:20 - 10:50 AM</b>IP Presentations</li>
          <li><b>11:00 - 11:45 AM</b>Breakout Sessions</li>
          <li><b>11:45 - 1:00 PM</b>Networking Lunch</li>
          <li style="min-height:36px"><b>1:00 - 2:35 PM</b>Solution Provider Demos<small>*5 Rounds, 15 min rotations,<br>5 min in between</small></li>
          <li><b>2:45 - 3:30 PM</b>Breakout Sessions</li>
          <li><b>3:40 - 4:10 PM</b>IP Presentations</li>
          <li style="min-height:28px"><b>4:10 - 4:30 PM</b>Break</li>
          <li><b>4:30 - 5:15 PM</b>Keynote Speaker</li>
          <li><b>5:15 - 6:30 PM</b>Networking Reception &amp;<br>Hors d’ouvres</li>
          <li><b>6:30 PM</b>Open Dinner</li>
          <li><b>8:30 PM</b>Late Night Event</li>
        </ul>
      </div>

      <div class="day-col" style="left:297px">
        <div class="day-tab"><div>Wednesday<b>5/17</b></div><div>Main<b>Conference</b></div></div>
        <ul class="slots">
          <li><b>7:30 - 9:00 AM</b>Networking Breakfast</li>
          <li><b>9:00 - 9:45 AM</b>Keynote Speaker</li>
          <li><b>9:45 - 10:15 AM</b>Keynote Speaker</li>
          <li><b>10:15 - 10:30 AM</b>Break</li>
          <li><b>10:30 - 11:00 AM</b>IP Presentations</li>
          <li><b>11:10 - 11:55 AM</b>Breakout Sessions</li>
          <li><b>11:55 - 1:30 PM</b>Networking Lunch</li>
          <li><b>1:30 - 3:30 PM</b>Case Study Workshops</li>
          <li><b>3:30 - 4:15 PM</b>Keynote Speaker</li>
          <li><b>4:15 - 4:30 PM</b>Closing Remarks</li>
        </ul>
      </div>

      <div class="brand-seal">TRV</div>
    </div>

    <div class="abs lineup">
      <div class="speaker" style="left:47px;top:34px">
        <div class="portrait" role="img" aria-label="Speaker portrait"></div>
        <h4>Marlow &amp; Tessa Quinlan</h4>
        <div class="role">Broker Associate &amp; Realtor</div>
        <div class="cred">Graduate, Field Institute (FIG)<br>Certified Retail Strategy Specialist (CRSS)</div>
      </div>
      <div class="speaker" style="left:228px;top:34px">
        <div class="portrait" role="img" aria-label="Speaker portrait"></div>
        <h4>Marlow &amp; Tessa Quinlan</h4>
        <div class="role">Broker Associate &amp; Realtor</div>
        <div class="cred">Graduate, Field Institute (FIG)<br>Certified Retail Strategy Specialist (CRSS)</div>
      </div>
      <div class="speaker" style="left:47px;top:155px">
        <div class="portrait" role="img" aria-label="Speaker portrait"></div>
        <h4>Marlow &amp; Tessa Quinlan</h4>
        <div class="role">Broker Associate &amp; Realtor</div>
        <div class="cred">Graduate, Field Institute (FIG)<br>Certified Retail Strategy Specialist (CRSS)</div>
      </div>
      <div class="speaker" style="left:228px;top:155px">
        <div class="portrait" role="img" aria-label="Speaker portrait"></div>
        <h4>Marlow &amp; Tessa Quinlan</h4>
        <div class="role">Broker Associate &amp; Realtor</div>
        <div class="cred">Graduate, Field Institute (FIG)<br>Certified Retail Strategy Specialist (CRSS)</div>
      </div>
    </div>

    <div class="abs promo">
      <div class="stat-box" style="left:16px">Include 2 pop up areas that we can put in a statistic</div>
      <div class="stat-box" style="left:151px">Include 2 pop up areas that we can put in a statistic</div>
      <div class="discount"><b>10%</b><span>DISCOUNT</span><small>ON<br>REGISTRATION</small></div>
      <p class="promo-note">Register Now and Receive 10% off your conference registration</p>
    </div>

    <div class="abs sponsors" aria-label="Partner badges">
      <i></i><i></i><i></i><i class="round"></i><i></i><i></i><i></i><i></i><i class="round"></i><i></i>
    </div>
  </section>

</main>
</body>
</html>
```